Lavoie Roofing

Want a professional looking business card

Industry/Entity Type

Business

Contact Information for Business Card

Mark Lavoie ( Owner) mark@lavoieroofing.example, www.lavoieroofing.example, Adress: 4712 County road 31 Pinecrest Falls, ON Z0Z 2M4

```html
<!DOCTYPE html>
<html lang="en">
<head>
<meta charset="utf-8">
<title>Lavoie Roofing – Business Card</title>
<link rel="stylesheet" href="https://fonts.googleapis.com/css2?family=Roboto:wght@400&family=Saira+Semi+Condensed:wght@600;700&display=swap">
<style>
  :root {
    --backdrop: #2b2b2b;
    --card-white: #f4f4f4;
    --brand-blue: #174280;
    --brand-grey: #808080;
    --text-dark: #474747;
    --text-light: #ffffff;
  }
  * { box-sizing: border-box; margin: 0; padding: 0; }
  html, body { width: 1200px; height: 960px; overflow: hidden; }
  body { background: var(--backdrop); position: relative; }

  .card { position: absolute; width: 600px; height: 343px; }
  .card-front { left: 314px; top: 113px; background: var(--card-white); }
  .card-back { left: 311px; top: 472px; height: 342px; background: var(--brand-blue); }

  .name-band { position: absolute; left: 0; top: 44px; width: 516px; height: 56px; background: var(--brand-blue); }
  .grey-band { position: absolute; left: 516px; top: 44px; width: 84px; height: 56px; background: var(--brand-grey); }

  .owner-name {
    position: absolute; left: 36px; top: 52px;
    font-family: "Saira Semi Condensed", sans-serif; font-weight: 600;
    font-size: 22px; line-height: 24px; color: var(--text-light); letter-spacing: 0.2px;
  }
  .owner-title {
    position: absolute; left: 36px; top: 78px;
    font-family: "Saira Semi Condensed", sans-serif; font-weight: 600;
    font-size: 14px; line-height: 16px; color: var(--text-light); letter-spacing: 0.5px;
  }

  .company-name {
    position: absolute; right: 36px; top: 112px;
    font-family: "Saira Semi Condensed", sans-serif; font-weight: 700;
    font-size: 30px; line-height: 34px; color: var(--brand-blue); letter-spacing: 1px;
  }

  .contact-list { position: absolute; left: 36px; top: 255px; list-style: none; }
  .contact-list li {
    display: flex; align-items: center; gap: 8px; height: 19px;
    font-family: "Roboto", sans-serif; font-size: 14px; color: var(--text-dark);
  }
  .contact-list svg { width: 13px; height: 13px; fill: var(--brand-blue); flex: none; }

  .address {
    position: absolute; right: 36px; top: 274px; text-align: right; font-style: normal;
    font-family: "Roboto", sans-serif; font-size: 14px; line-height: 19px; color: var(--text-dark);
  }

  .back-company {
    position: absolute; left: 0; right: 0; top: 140px; text-align: center;
    font-family: "Saira Semi Condensed", sans-serif; font-weight: 700;
    font-size: 54px; line-height: 60px; color: var(--text-light); letter-spacing: 2px;
  }
  .back-url {
    position: absolute; left: 0; right: 0; top: 284px; text-align: center;
    font-family: "Roboto", sans-serif; font-size: 15px; color: var(--text-light); letter-spacing: 5px;
  }
</style>
</head>
<body>
  <section class="card card-front">
    <div class="name-band"></div>
    <div class="grey-band"></div>
    <h1 class="owner-name">MARK LAVOIE</h1>
    <p class="owner-title">OWNER</p>
    <p class="company-name">LAVOIE ROOFING</p>

    <ul class="contact-list">
      <li>
        <svg viewBox="0 0 16 16" aria-hidden="true"><path d="M3.6 1.2l2.3 2.6c.4.4.4 1 0 1.4L4.8 6.4c.9 2 2.6 3.8 4.8 4.8l1.2-1.1c.4-.4 1-.4 1.4 0l2.6 2.3c.4.4.4 1 0 1.4l-1.4 1.3c-.6.6-1.5.7-2.3.4C6.4 13.7 2.3 9.6.5 4.9.2 4.1.4 3.2 1 2.6l1.3-1.4c.4-.4 1-.4 1.3 0z"/></svg>
        555 014 2290
      </li>
      <li>
        <svg viewBox="0 0 16 16" aria-hidden="true"><path d="M1 3h14v1.2L8 8.6 1 4.2z"/><path d="M1 5.6l7 4.4 7-4.4V13H1z"/></svg>
        mark@lavoieroofing.example
      </li>
      <li>
        <svg viewBox="0 0 16 16" aria-hidden="true"><circle cx="8" cy="8" r="7"/><path d="M5 4.5c1.5.2 2.5 1.3 2 2.6-.4 1-1.8.9-2 2.2-.2 1.1.6 2 .3 3.4M10.5 3.5c-.8 1-.3 2 .7 2.3 1 .3 1.6 1.5 1 2.6" stroke="#f4f4f4" stroke-width="1.2" fill="none"/></svg>
        www.lavoieroofing.example
      </li>
    </ul>

    <address class="address">4712 County road 31<br>Pinecrest Falls, ON Z0Z 2M4</address>
  </section>

  <section class="card card-back">
    <p class="back-company">LAVOIE ROOFING</p>
    <p class="back-url">www.lavoieroofing.example</p>
  </section>
</body>
</html>
```